Dynamic and Revolutionary Training Company Requires Stationery Design Project

We are a training company who deliver training both online and face to face.

We train in:
~ Industry Training: Earth Moving Machinery, Cranes, Work at Heights, Confined Spaces, Elevating Work Platforms, Forklift etc.
~ Food Hygiene / Safety
~ Responsible Service of Alcohol / Gambling

Our company is interested in sourcing stationery designs for:

* Pens
These will be used in classroom training courses but also given away in advertising 'packs'

* Presentation folders
These can be either bi or tri fold cardboard folders. Promotional materials / leaflets will be placed inside these folders and given away in advertising 'packs'

* Letterhead
We need to update our old / outdated letterhead

* Exercise Book Covers
These exercise books will be used by students in our face to face training courses.

* With Compliments Slip
In 100+ envelopes we send each day we currently add a business card. We are now going to add a with with compliments slip with an offer / promotion instead.

* Pull Up Banner
Front of stall display at expos / trade shows.

* Flyers
We would like a template design for a DL sized flyer. We offer training in over 30 courses, so if we had a standard template that could be adapted to each training course we would achieve consistency in advertising.
Flyers would need the same / similar front (with space for a picture) and course information could be placed on the back.

Because of our extensive (and ever expanding) scope of training, certain products (folders, exercise books) will allow us to list some / all our training courses.
Other advertising mediums will obviously only allow us to display our logo and slogan (pens etc).

Please find attached our company logo.
Company slogan -
Updates

Good Morning All,

I apologise for this glaring oversight.

I unfortunately failed to mention that our primary 'business colour' (obviously outside the logo) is blue. 

Traditionally, the blue I refer to is a lightish blue as can be seen on our website banner: www.quorvatraining.edu.au 
We are however moving into a new premises which has navy blue carpet, so we would like to move more towards a navy blue.

We would also like to adjust several sliders, significantly more towards:
* elegant
* personable

And somewhat more towards:
* colourful

Sorry for any inconvenience designers :(

Regards,
Tom

Closing day tomorrow.

Only received designs from 2 designers thus far.

Last chance today to submit designs.............................

Target Market(s)

Employed / unemployed persons looking to upskill, companies / organisations looking for a quality training provider.

Industry/Entity Type

Advertising

Requirements
Must have
• More than happy to be guided by designer.

I would like to see the letterhead also involve a footer - of some sort.

Logo colours are original since company inception so must remain.

Slogan - we do have one, however our advertising has never had it as a major focus.
Nice to have
• Most written correspondence we send via email (statements of attainment, invoices etc) has a Quorva Training watermark across it.
If possible and it looks appropriate in your opinion, the larger advertising (folders, exercise books) could MAYBE have that as well.

```html
<!DOCTYPE html>
<html lang="en">
<head>
<meta charset="utf-8">
<title>Quorva Training Stationery</title>
<link href="https://fonts.googleapis.com/css2?family=Open+Sans:wght@400;600;700&display=swap" rel="stylesheet">
<style>
  :root {
    --olive: #9d9c34;
    --charcoal: #2f2f30;
    --charcoal-light: #4a4a4b;
    --paper: #ffffff;
    --ink: #1e1e1e;
    --backdrop: #e6e4df;
  }
  * { margin: 0; padding: 0; box-sizing: border-box; }
  html, body { width: 1200px; height: 784px; overflow: hidden; }
  body {
    background: var(--backdrop);
    font-family: "Open Sans", Arial, sans-serif;
    color: var(--ink);
    position: relative;
  }
  .sheet { position: absolute; background: var(--paper); overflow: hidden; box-shadow: 0 1px 3px rgba(0,0,0,.15); }
  .swoosh { position: absolute; left: 0; width: 100%; display: block; }

  .brand { display: flex; align-items: center; gap: 8px; }
  .brand-mark { background: var(--olive); flex: none; }
  .brand-name { color: var(--olive); font-weight: 700; text-transform: uppercase; letter-spacing: .02em; white-space: nowrap; }

  .contact-line { display: flex; align-items: center; gap: 6px; white-space: nowrap; }
  .contact-line svg { width: 8px; height: 8px; fill: var(--olive); flex: none; }

  /* Letterhead */
  .letterhead { left: 16px; top: 12px; width: 574px; height: 760px; }
  .letterhead .brand { position: absolute; left: 24px; top: 78px; }
  .letterhead .brand-mark { width: 26px; height: 26px; }
  .letterhead .brand-name { font-size: 22px; }
  .letterhead-contact { position: absolute; left: 300px; top: 8px; font-size: 8.5px; line-height: 12px; }
  .letterhead-contact .address { margin-top: 3px; }
  .letterhead-contact .reg { margin-top: 3px; }
  .letterhead .swoosh { bottom: 0; height: 150px; }

  /* Business card front */
  .card-front { left: 438px; top: 108px; width: 392px; height: 186px; }
  .card-front .swoosh { top: 0; height: 186px; }
  .card-front .brand { position: absolute; left: 22px; top: 60px; }
  .card-front .brand-mark { width: 18px; height: 18px; }
  .card-front .brand-name { font-size: 16px; }
  .card-holder { position: absolute; right: 46px; top: 18px; text-align: right; }
  .card-holder .name { color: var(--olive); font-weight: 700; font-size: 13px; }
  .card-holder .role { font-size: 9px; }
  .card-contact { position: absolute; right: 22px; top: 96px; text-align: right; font-size: 9px; line-height: 12.5px; color: #fff; }
  .card-contact .contact-line { justify-content: flex-end; }
  .card-contact .contact-line svg { fill: #fff; }
  .card-contact .address { margin-top: 6px; }
  .card-reg { position: absolute; left: 46px; bottom: 10px; font-size: 7.5px; color: #fff; }

  /* Business card back */
  .card-back { left: 850px; top: 0; width: 350px; height: 250px;
    background: radial-gradient(ellipse at 55% 45%, var(--charcoal-light), var(--charcoal) 70%); }
  .card-back .brand { position: absolute; left: 0; right: 0; top: 108px; justify-content: center; }
  .card-back .brand-mark { width: 20px; height: 20px; }
  .card-back .brand-name { font-size: 20px; }
  .card-back .web { position: absolute; left: 0; right: 0; top: 182px; text-align: center; color: var(--olive); font-size: 9px; letter-spacing: .2em; }

  /* Envelope back */
  .envelope-back { left: 568px; top: 300px; width: 632px; height: 146px; background: var(--paper); }
  .envelope-back .flap { position: absolute; left: 0; top: 0; width: 100%; height: 100%; display: block; }
  .envelope-back .brand { position: absolute; left: 0; right: 0; justify-content: center; }
  .envelope-back .brand-mark { width: 16px; height: 16px; }
  .envelope-back .brand-name { font-size: 16px; }
  .envelope-back .on-paper { top: 10px; }
  .envelope-back .on-flap { top: 98px; }

  /* Envelope front */
  .envelope-front { left: 568px; top: 456px; width: 632px; height: 328px; }
  .envelope-front .brand { position: absolute; left: 60px; top: 86px; }
  .envelope-front .brand-mark { width: 14px; height: 14px; }
  .envelope-front .brand-name { font-size: 13px; }
  .envelope-front .return { position: absolute; left: 68px; top: 136px; font-size: 7px; }
  .address-window { position: absolute; left: 72px; top: 152px; width: 160px; height: 52px;
    border: 1px dashed #bdbdbd; border-radius: 8px; background: #f1f1f1; }
  .envelope-front .swoosh { bottom: 0; height: 200px; }
</style>
</head>
<body>

<svg width="0" height="0" style="position:absolute">
  <defs>
    <symbol id="icon-phone" viewBox="0 0 10 10"><path d="M1 3c0-2 8-2 8 0v1H7V3H3v1H1zM2 5h6l1 4H1z"/></symbol>
    <symbol id="icon-fax" viewBox="0 0 10 10"><path d="M3 0h4v3H3zM0 3h10v5H8v2H2V8H0z"/></symbol>
    <symbol id="icon-mail" viewBox="0 0 10 10"><path d="M5 0a5 5 0 1 0 3 9l-.6-.8A4 4 0 1 1 9 5v1a1 1 0 0 1-2 0V3H6v.4A2 2 0 1 0 6.8 7 2 2 0 0 0 10 6V5A5 5 0 0 0 5 0zm0 4a1 1 0 1 1 0 2 1 1 0 0 1 0-2z"/></symbol>
    <symbol id="icon-web" viewBox="0 0 10 10"><path d="M5 0a5 5 0 1 0 0 10A5 5 0 0 0 5 0zm0 1.2a3.8 3.8 0 1 1 0 7.6 3.8 3.8 0 0 1 0-7.6zM4 3l3 2-3 2z"/></symbol>
  </defs>
</svg>

<!-- Letterhead -->
<section class="sheet letterhead">
  <div class="brand"><span class="brand-mark"></span><span class="brand-name">Quorva Training</span></div>
  <div class="letterhead-contact">
    <div class="contact-line"><svg><use href="#icon-phone"/></svg>(07) 4100 2231</div>
    <div class="contact-line"><svg><use href="#icon-fax"/></svg>(07) 4100 2298</div>
    <div class="contact-line"><svg><use href="#icon-mail"/></svg>support@quorvatraining.edu.au</div>
    <div class="contact-line"><svg><use href="#icon-web"/></svg>www.quorvatraining.edu.au</div>
    <div class="address">Box 5120, Harbourview South<br>Queensland 4690</div>
    <div class="reg">ABN: 12 345 678 901 - RTO: 40217</div>
  </div>
  <svg class="swoosh" viewBox="0 0 574 150" preserveAspectRatio="none">
    <path d="M0 122 C160 110 380 50 574 8 L574 16 C380 60 170 118 0 132Z" fill="var(--olive)"/>
    <path d="M0 134 C180 118 390 62 574 26 L574 150 L0 150Z" fill="var(--charcoal)"/>
    <path d="M0 140 C190 124 400 68 574 36 L574 40 C400 74 190 130 0 144Z" fill="#fff"/>
  </svg>
</section>

<!-- Business card front -->
<section class="sheet card-front">
  <svg class="swoosh" viewBox="0 0 392 186" preserveAspectRatio="none">
    <path d="M0 128 C130 136 230 62 392 32 L392 42 C232 72 132 146 0 138Z" fill="var(--olive)"/>
    <path d="M0 146 C130 152 230 80 392 56 L392 186 L0 186Z" fill="var(--charcoal)"/>
    <path d="M0 152 C132 158 234 88 392 66 L392 69 C234 91 132 161 0 155Z" fill="#fff"/>
  </svg>
  <div class="card-holder"><div class="name">Martin Hale</div><div class="role">President</div></div>
  <div class="brand"><span class="brand-mark"></span><span class="brand-name">Quorva Training</span></div>
  <div class="card-contact">
    <div class="contact-line">(07) 4100 2231 <svg><use href="#icon-phone"/></svg></div>
    <div class="contact-line">(07) 4100 2298 <svg><use href="#icon-fax"/></svg></div>
    <div class="contact-line">support@quorvatraining.edu.au <svg><use href="#icon-mail"/></svg></div>
    <div class="contact-line">www.quorvatraining.edu.au <svg><use href="#icon-web"/></svg></div>
    <div class="address">Box 5120, Harbourview South<br>Queensland 4690</div>
  </div>
  <div class="card-reg">ABN: 12 345 678 901 - RTO: 40217</div>
</section>

<!-- Business card back -->
<section class="sheet card-back">
  <div class="brand"><span class="brand-mark"></span><span class="brand-name">Quorva Training</span></div>
  <div class="web">www.quorvatraining.edu.au</div>
</section>

<!-- Envelope back -->
<section class="sheet envelope-back">
  <svg class="flap" viewBox="0 0 632 146" preserveAspectRatio="none">
    <path d="M0 60 L632 36 L632 116 Q632 146 600 144 L200 144 Q40 144 20 100 Z" fill="var(--charcoal)"/>
  </svg>
  <div class="brand on-paper"><span class="brand-mark"></span><span class="brand-name">Quorva Training</span></div>
  <div class="brand on-flap"><span class="brand-mark"></span><span class="brand-name">Quorva Training</span></div>
</section>

<!-- Envelope front -->
<section class="sheet envelope-front">
  <div class="brand"><span class="brand-mark"></span><span class="brand-name">Quorva Training</span></div>
  <div class="return">Box 5120, Harbourview South, Queensland 4690</div>
  <div class="address-window"></div>
  <svg class="swoosh" viewBox="0 0 632 200" preserveAspectRatio="none">
    <path d="M0 150 C200 130 420 40 632 20 L632 30 C420 52 210 140 0 162Z" fill="var(--olive)"/>
    <path d="M0 168 C210 148 430 62 632 44 L632 200 L0 200Z" fill="var(--charcoal)"/>
    <path d="M0 174 C220 154 440 70 632 54 L632 58 C440 76 220 160 0 178Z" fill="#fff"/>
  </svg>
</section>

</body>
</html>
```